Velko
trosen
Use same font as used in my logo
Yousef Harbi يوسف حربي
General manager المدير العام
P.O.Box 48735 Riyadh 13542
Saudi Arabia
ص.ب 48735 الرياض 13542
المملكة العربية السعودية
Info@velkohouse.example
www.velkohouse.example
C.R. 1049728513 CC.487139
I want to be design Arabic & English

```html
<!DOCTYPE html>
<html lang="en">
<head>
<meta charset="utf-8">
<title>Velko Stationery</title>
<link href="https://fonts.googleapis.com/css2?family=Cairo:wght@400;600;700&display=swap" rel="stylesheet">
<style>
  :root{
    --brand:#2c63b4;
    --brand-dark:#1f4c8f;
    --paper:#ffffff;
    --ink:#3d4350;
    --muted:#9aa1ad;
    --stage:#d8d9dc;
    --panel:#f4f5f7;
  }
  *{box-sizing:border-box;margin:0;padding:0}
  html,body{width:1200px;height:240px;overflow:hidden}
  body{background:var(--stage);font-family:"Cairo",sans-serif;color:var(--ink);position:relative}
  .item{position:absolute;background:var(--paper);overflow:hidden}
  .blue{background:var(--brand);color:#fff}
  .logo{display:flex;flex-direction:column;align-items:center;gap:2px;color:var(--brand)}
  .logo .mark{border:2px solid currentColor;border-radius:50%}
  .logo .name{font-weight:700;letter-spacing:.12em;text-transform:uppercase;line-height:1}
  .blue .logo{color:#fff}
  .center{display:flex;align-items:center;justify-content:center}
  .tiny{font-size:4px;line-height:1.4;white-space:nowrap}
  .small{font-size:5px;line-height:1.4}
  .rtl{direction:rtl;text-align:right}
  bdi{unicode-bidi:isolate}
  .bar{position:absolute;left:0;right:0;height:4px;background:var(--brand)}
  .footer{position:absolute;left:8px;right:8px;display:flex;justify-content:space-between;color:var(--muted)}
  .body-text{position:absolute;left:12px;right:12px;top:60px;font-size:5px;line-height:1.6;color:var(--ink)}
  .flap{position:absolute;left:0;top:0;width:100%;height:100%}
</style>
</head>
<body>

<!-- Brand card -->
<div class="item brand-card center" style="left:12px;top:10px;width:200px;height:130px">
  <div class="logo"><span class="mark" style="width:34px;height:34px"></span><span class="name" style="font-size:16px">Velko</span></div>
</div>

<!-- Business cards -->
<div class="item blue bizcard-front center" style="left:12px;top:150px;width:96px;height:40px">
  <div class="logo"><span class="mark" style="width:12px;height:12px"></span><span class="name" style="font-size:7px">Velko</span></div>
</div>
<div class="item bizcard-back" style="left:114px;top:150px;width:98px;height:40px;padding:5px 5px">
  <div class="bar" style="top:0;height:3px"></div>
  <div style="display:flex;justify-content:space-between">
    <div class="tiny"><b>Yousef Harbi</b><br>General manager</div>
    <div class="tiny rtl" lang="ar"><b>يوسف حربي</b><br>المدير العام</div>
  </div>
  <div class="tiny" style="margin-top:3px;color:var(--muted)">Info@velkohouse.example<br>www.velkohouse.example</div>
</div>
<div class="item bizcard-front-white center" style="left:12px;top:196px;width:96px;height:40px">
  <div class="logo"><span class="mark" style="width:12px;height:12px"></span><span class="name" style="font-size:7px">Velko</span></div>
</div>
<div class="item bizcard-back" style="left:114px;top:196px;width:98px;height:40px;padding:5px 5px">
  <div class="tiny"><b>Yousef Harbi</b> · General manager</div>
  <div class="tiny">P.O.Box 48735 Riyadh 13542, Saudi Arabia</div>
  <div class="tiny rtl" lang="ar"><bdi>ص.ب 48735 الرياض 13542</bdi> <bdi>المملكة العربية السعودية</bdi></div>
  <div class="bar" style="bottom:0;height:3px"></div>
</div>

<!-- Letterhead A -->
<div class="item letterhead" style="left:228px;top:8px;width:130px;height:224px">
  <div class="logo" style="margin-top:12px"><span class="mark" style="width:18px;height:18px"></span><span class="name" style="font-size:8px">Velko</span></div>
  <p class="body-text">Dear Client,<br>Thank you for your continued trust in our services.</p>
  <div class="footer tiny" style="bottom:10px"><span>P.O.Box 48735 Riyadh 13542</span><span class="rtl" lang="ar"><bdi>ص.ب 48735 الرياض 13542</bdi></span></div>
  <div class="bar" style="bottom:0"></div>
</div>

<!-- Letterhead B -->
<div class="item letterhead" style="left:370px;top:8px;width:130px;height:224px">
  <div class="logo" style="margin-top:12px"><span class="mark" style="width:18px;height:18px"></span><span class="name" style="font-size:8px">Velko</span></div>
  <p class="body-text">We look forward to working with you.<br><br>Best regards<br><b>Yousef Harbi</b><br>General manager</p>
  <div class="footer tiny" style="bottom:10px;font-size:3.6px"><span>Info@velkohouse.example</span><span>C.R. 1049728513 · CC.487139</span></div>
  <div class="bar" style="bottom:0"></div>
</div>

<!-- Compliment slip -->
<div class="item slip" style="left:512px;top:8px;width:140px;height:70px">
  <div class="bar" style="top:0;height:18px"></div>
  <div class="logo" style="position:absolute;left:0;right:0;top:24px"><span class="mark" style="width:12px;height:12px"></span><span class="name" style="font-size:6px">Velko</span></div>
  <div class="small" style="position:absolute;bottom:6px;left:0;right:0;text-align:center;color:var(--brand)">With Compliments</div>
</div>

<!-- Small cards -->
<div class="item center" style="left:512px;top:88px;width:66px;height:36px">
  <div class="logo"><span class="mark" style="width:10px;height:10px"></span><span class="name" style="font-size:5px">Velko</span></div>
</div>
<div class="item" style="left:586px;top:88px;width:66px;height:36px;padding:4px">
  <div class="tiny" style="font-size:3.8px"><b>Yousef Harbi</b><br>www.velkohouse.example</div>
  <div class="bar" style="bottom:0;height:3px"></div>
</div>

<!-- Envelopes -->
<div class="item envelope" style="left:664px;top:8px;width:240px;height:104px">
  <svg class="flap" viewBox="0 0 240 104" preserveAspectRatio="none" aria-hidden="true">
    <polyline points="0,0 120,48 240,0" fill="none" stroke="#e3e5e9" stroke-width="1"/>
  </svg>
  <div class="logo" style="position:absolute;left:10px;top:58px"><span class="mark" style="width:12px;height:12px"></span><span class="name" style="font-size:6px">Velko</span></div>
  <div class="tiny" style="position:absolute;left:10px;bottom:9px;color:var(--muted)">P.O.Box 48735 Riyadh 13542 · Saudi Arabia</div>
  <div class="bar" style="bottom:0;height:3px"></div>
</div>
<div class="item envelope" style="left:664px;top:122px;width:240px;height:108px">
  <svg class="flap" viewBox="0 0 240 108" preserveAspectRatio="none" aria-hidden="true">
    <polygon points="0,0 240,0 120,46" fill="var(--brand)"/>
  </svg>
  <div class="logo" style="position:absolute;left:0;right:0;top:58px"><span class="mark" style="width:12px;height:12px"></span><span class="name" style="font-size:6px">Velko</span></div>
  <div class="tiny rtl" lang="ar" style="position:absolute;right:10px;bottom:8px;color:var(--muted)"><bdi>ص.ب 48735 الرياض 13542</bdi> · <bdi>المملكة العربية السعودية</bdi></div>
</div>

<!-- Folder -->
<div class="item folder-inside" style="left:916px;top:8px;width:138px;height:224px;background:var(--panel)">
  <div style="position:absolute;left:0;right:0;bottom:0;height:80px;background:var(--brand)"></div>
</div>
<div class="item blue folder-cover center" style="left:1054px;top:8px;width:138px;height:224px;flex-direction:column">
  <div class="logo"><span class="mark" style="width:34px;height:34px"></span><span class="name" style="font-size:12px">Velko</span></div>
  <div class="tiny" style="position:absolute;bottom:8px;opacity:.8">www.velkohouse.example</div>
</div>

</body>
</html>
```